Meridian Handsets business card design

I would like to see some designs for a business card for Meridian Handsets. I would like the business card to be double sided. It will need to have a similar colour / look and feel to our website www.meridianhandsets.com.au I have also attached our latest flyer. Final designs to be handed over in Photoshop format so that I can edit the business card when needed please.

Industry/Entity Type

Business

Contact Information for Business Card

Gavin Thornley
sales@meridianhandsets.com.au
Business Development Manager
ph: (08) 6197 5821
www.meridianhandsets.com.au

Font styles to use
Serif
Sans Serif

Requirements
Must have
• If you could please utilise our colour scheme as seen on our website and the attached flyer.
• I would also like the final design to be in a Photoshop format so that I can edit it when needed please.

```html
<!DOCTYPE html>
<html lang="en">
<head>
<meta charset="utf-8">
<title>Meridian Handsets – Business Card</title>
<link rel="stylesheet" href="https://fonts.googleapis.com/css2?family=Montserrat:wght@500&family=Lato:wght@400;700&display=swap">
<style>
  :root {
    --page-bg: #2b2b2d;
    --teal: #17a48c;
    --teal-deep: #1b7f74;
    --ribbon-blue: #1f6fae;
    --ribbon-navy: #2c4a8c;
    --ink: #2d2d2f;
    --white: #ffffff;
    --paper: #f4f4f4;
  }
  html, body {
    margin: 0;
    width: 1200px;
    height: 997px;
    overflow: hidden;
    background: var(--page-bg);
  }
  .canvas {
    position: relative;
    width: 1200px;
    height: 997px;
  }
  .card {
    position: absolute;
    width: 560px;
    height: 320px;
    border-radius: 22px;
    overflow: hidden;
    box-shadow: 0 18px 40px rgba(0,0,0,.45);
  }

  /* Back side */
  .card-back {
    left: 80px;
    top: 110px;
  }
  .card-back .facet-fill {
    position: absolute;
    inset: 0;
    background: linear-gradient(135deg, #3ab9a2 0%, var(--teal) 45%, var(--teal-deep) 100%);
  }
  .card-back .brand-name {
    position: absolute;
    left: 0;
    right: 0;
    top: 132px;
    text-align: center;
    font-family: "Montserrat", sans-serif;
    font-weight: 500;
    font-size: 44px;
    color: var(--white);
    letter-spacing: .5px;
  }

  /* Front side */
  .card-front {
    left: 560px;
    top: 500px;
    background: var(--paper);
  }
  .card-front svg.front-shapes {
    position: absolute;
    inset: 0;
  }
  .card-front .brand-name {
    position: absolute;
    left: 52px;
    top: 52px;
    font-family: "Montserrat", sans-serif;
    font-weight: 500;
    font-size: 38px;
    color: var(--ink);
  }
  .card-front .holder {
    position: absolute;
    left: 150px;
    top: 135px;
    font-family: "Lato", sans-serif;
    line-height: 1.1;
  }
  .holder .holder-name {
    color: var(--white);
    font-size: 19px;
    letter-spacing: .5px;
    text-transform: uppercase;
  }
  .holder .holder-role {
    color: #10213a;
    font-size: 13px;
    font-weight: 700;
  }
  .contact-list {
    position: absolute;
    left: 38px;
    top: 212px;
    margin: 0;
    padding: 0;
    list-style: none;
    font-family: "Lato", sans-serif;
    font-size: 15px;
    color: var(--white);
  }
  .contact-list li {
    display: flex;
    align-items: center;
    gap: 12px;
    height: 27px;
  }
  .contact-list svg {
    width: 14px;
    height: 14px;
    fill: #0e3d36;
  }
  .brand-dot {
    position: absolute;
    right: 64px;
    top: 200px;
    width: 64px;
    height: 64px;
    border-radius: 50%;
    background: rgba(255,255,255,.55);
  }
</style>
</head>
<body>
<main class="canvas">

  <section class="card card-back" aria-label="Business card, back side">
    <div class="facet-fill" role="img" aria-label="Teal low-poly faceted background pattern"></div>
    <div class="brand-name">Meridian Handsets</div>
  </section>

  <section class="card card-front" aria-label="Business card, front side">
    <svg class="front-shapes" width="560" height="320" viewBox="0 0 560 320">
      <defs>
        <linearGradient id="tealBand" x1="0" y1="0" x2="1" y2="1">
          <stop offset="0" stop-color="#10c596"/>
          <stop offset="1" stop-color="#1a9c8a"/>
        </linearGradient>
      </defs>
      <rect class="teal-band" x="0" y="172" width="560" height="148" fill="url(#tealBand)"/>
      <rect class="edge-line" x="0" y="167" width="560" height="5" fill="var(--ribbon-navy)"/>
      <polygon class="ribbon-fold" points="84,190 114,172 150,172" fill="var(--ribbon-navy)"/>
      <polygon class="ribbon-fold" points="430,130 500,150 466,172" fill="var(--ribbon-navy)"/>
      <polygon class="ribbon" points="132,130 448,130 470,172 110,172" fill="var(--ribbon-blue)"/>
    </svg>

    <div class="brand-name">Meridian Handsets</div>

    <div class="holder">
      <div class="holder-name">Gavin Thornley</div>
      <div class="holder-role">Business Development Manager</div>
    </div>

    <div class="brand-dot"></div>

    <ul class="contact-list">
      <li>
        <svg viewBox="0 0 14 14"><path d="M4 0h6a1 1 0 0 1 1 1v12a1 1 0 0 1-1 1H4a1 1 0 0 1-1-1V1a1 1 0 0 1 1-1zm0 2v9h6V2z"/></svg>
        (08) 6197 5821
      </li>
      <li>
        <svg viewBox="0 0 14 14"><path d="M0 3h14v9H0zM0 3l7 5 7-5v1.5L7 9.5 0 4.5z"/></svg>
        sales@meridianhandsets.com.au
      </li>
      <li>
        <svg viewBox="0 0 14 14"><path d="M7 0a7 7 0 1 1 0 14A7 7 0 0 1 7 0zm0 2a5 5 0 1 0 0 10A5 5 0 0 0 7 2zM2 6.5h10v1H2zM6.5 2h1v10h-1z"/></svg>
        www.meridianhandsets.com.au
      </li>
    </ul>
  </section>

</main>
</body>
</html>
```